Fundraising campaign to raise money to purchase a pub

We are a voluntary group campaigning to stop a pub from becoming residential flats by fighting planning proposals. We are also raising money to buy or lease the pub to re-open it as a community pub.I have attached a mock idea for a flyer.We are seeking a flyer that we can use to handout.

The purpose of the flyer is to invite people to our public meeting and to complete our pub survey.

We are looking for an A5 flyer in terms of size

Target Market(s)

Local residents, investors

Industry/Entity Type

Residential

Font styles to use
Serif
Sans Serif
Decorative
Script

Requirements
Must have
• Be eyecatching. Must have a summary of the campaign. Must also have website date and time of the public meeting. Must also promote the survey and website. Must also have contact details. Must have the survey. The date and the survey should be easily spotted.
Nice to have
• A picture of the plough
Should not have
• Clip art

```html
<!DOCTYPE html>
<html lang="en">
<head>
<meta charset="UTF-8">
<title>Safeguarding the Future of The Plough</title>
<link rel="stylesheet" href="https://fonts.googleapis.com/css2?family=Cinzel:wght@700;900&family=Playfair+Display:wght@700&family=Dancing+Script:wght@600&family=Amatic+SC:wght@700&family=Open+Sans:wght@400;600;700&family=Oswald:wght@500;600&display=swap">
<style>
  :root{
    --frame-brown:#5a3416;
    --deep-brown:#3a200c;
    --amber:#e8961e;
    --gold:#f3b531;
    --cream:#fff6e6;
    --ink:#3b2412;
    --white:#ffffff;
  }
  html,body{margin:0;padding:0;overflow:hidden;background:#eee;}
  .flyer{
    position:relative;width:889px;height:1200px;overflow:hidden;
    background:var(--white);box-sizing:border-box;
    border:14px solid var(--frame-brown);
    box-shadow:inset 0 0 0 4px var(--amber);
  }
  .masthead{position:absolute;top:70px;left:0;right:0;text-align:center;}
  .masthead h1{
    margin:0;font-family:"Cinzel",serif;font-weight:900;font-size:33px;
    color:var(--amber);line-height:1.1;white-space:nowrap;
    text-shadow:1px 1px 0 #a45d0a;
  }
  .masthead .tagline{
    margin:6px 0 0;font-family:"Playfair Display",serif;font-weight:700;
    font-size:27px;color:var(--ink);
  }
  .pub-photo{
    position:absolute;top:196px;left:36px;right:36px;height:450px;
    border-radius:34px 34px 0 0;
    background:linear-gradient(180deg,#d9d4cb 0%,#a79c8f 35%,#2a2622 60%,#3a342c 85%,#8b8376 100%);
  }
  .swoosh{position:absolute;left:0;top:560px;width:861px;height:140px;}
  .campaign-panel{
    position:absolute;left:0;right:0;top:698px;height:334px;
    background:var(--deep-brown);
  }
  .summary{position:absolute;left:28px;top:0;width:480px;}
  .summary .story{
    font-family:"Dancing Script",cursive;font-size:17px;line-height:1.3;
    color:var(--cream);margin:0 0 18px;
  }
  .summary .aim{
    font-family:"Amatic SC",cursive;font-weight:700;font-size:25px;line-height:1.12;
    color:var(--white);margin:0;letter-spacing:.3px;
  }
  .support{position:absolute;right:22px;top:-18px;width:302px;font-family:"Open Sans",sans-serif;color:var(--white);}
  .support h2{
    margin:0 0 4px;font-family:"Oswald",sans-serif;font-weight:600;font-size:19px;
    color:var(--gold);letter-spacing:.3px;white-space:nowrap;
  }
  .support p{margin:0 0 10px;font-size:13.5px;line-height:1.38;}
  .support .link{color:var(--gold);font-size:12px;white-space:nowrap;}
  .support .meeting{font-weight:700;font-size:15px;}
  .support .meeting .date{color:var(--gold);}
  .contact-band{
    position:absolute;left:0;right:0;bottom:0;height:140px;
    background:linear-gradient(180deg,#6b3e18,var(--frame-brown));
    border-top:4px solid var(--amber);text-align:center;color:var(--white);
  }
  .contact-band h2{
    margin:16px 0 12px;font-family:"Oswald",sans-serif;font-weight:600;font-size:34px;
    color:var(--gold);letter-spacing:1px;
  }
  .contact-row{display:flex;justify-content:space-between;padding:0 40px;font-family:"Open Sans",sans-serif;font-weight:700;font-size:22px;}
  .contact-row span{display:flex;align-items:center;gap:10px;}
  .contact-row svg{width:28px;height:28px;}
</style>
</head>
<body>
<div class="flyer">
  <header class="masthead">
    <h1>SAFEGUARDING THE FUTURE OF THE PLOUGH</h1>
    <p class="tagline">Protect pubs in South Norwood</p>
  </header>

  <div class="pub-photo" role="img" aria-label="Photograph of The Plough pub frontage on the high street"></div>

  <svg class="swoosh" viewBox="0 0 861 140" preserveAspectRatio="none" aria-hidden="true">
    <path d="M0 100 C260 40 560 150 861 50 L861 140 L0 140 Z" fill="#3a200c"/>
    <path d="M0 100 C260 40 560 150 861 50 L861 70 C560 170 260 60 0 122 Z" fill="#e8961e"/>
    <path d="M0 122 C260 60 560 170 861 70 L861 82 C560 182 260 74 0 134 Z" fill="#f3b531"/>
  </svg>

  <section class="campaign-panel">
    <div class="summary">
      <p class="story">The Plough, 48 Norwood High Street, SE25 was purchased by a property developer, who proceeded to gut the pub and convert it into seven flats. The developer has twice tried to obtain planning permission and now is the subject of retrospective planning to put the pub back downstairs and in the basement. Should this not be forthcoming Hollybrook Council will be issuing an enforcement notice to the owner.</p>
      <p class="aim">SAVE THE PLOUGH IS A CAMPAIGN TO PROTECT THE BUILDING AND ALSO RAISE MONEY TO LEASE THE PUB OR BUY THE BUILDING. WE WANT TO OPEN THE PLOUGH AS A COMMUNITY CO-OP PUB SERVING GREAT FOOD AND WINE.</p>
    </div>
    <div class="support">
      <h2>PLEASE SUPPORT OUR CAMPAIGN</h2>
      <p>by completing our survey<br><span class="link">survey.keepourlocal.example/plough</span><br>Paper copies of the survey are available, get a friend or relative to check on <span class="link">www.keepourlocal.example</span> for locations.</p>
      <p>Anyone wishing to find out more about our plans to open a great pub serving fantastic food and drinks can attend our meeting</p>
      <p class="meeting"><span class="date">August at 8pm at the</span><br>Harbour Inn, Linden Road, SE25</p>
    </div>
  </section>

  <footer class="contact-band">
    <h2>YOU CAN CONTACT US BY</h2>
    <div class="contact-row">
      <span>
        <svg viewBox="0 0 24 24" aria-hidden="true"><rect x="2" y="5" width="20" height="14" rx="2" fill="none" stroke="#f3b531" stroke-width="2"/><path d="M2 6 L12 13 L22 6" fill="none" stroke="#f3b531" stroke-width="2"/></svg>
        saveploughse25@mailbox.example
      </span>
      <span>
        <svg viewBox="0 0 24 24" aria-hidden="true"><path d="M6.6 10.8a15 15 0 0 0 6.6 6.6l2.2-2.2a1 1 0 0 1 1-.25 11.4 11.4 0 0 0 3.6.57 1 1 0 0 1 1 1V20a1 1 0 0 1-1 1A17 17 0 0 1 3 4a1 1 0 0 1 1-1h3.5a1 1 0 0 1 1 1c0 1.25.2 2.45.57 3.57a1 1 0 0 1-.25 1z" fill="#f3b531"/></svg>
        02080004172
      </span>
    </div>
  </footer>
</div>
</body>
</html>
```